Harlow Hauling | ||
Fine furniture transport and delivery service | ||
Use same font as used in my logo | ||
Cutting-Edge Modern Bright & Fun-filled |
Danny Crebbe | ||
Owner | ||
5810 County Road 7 Canaan,NH 03598 |
pinecarrier@velmorapost.net | ||
Looking for something that stands out. Maybe photo shop my logo into a 2008 or newer Korvath trekline van. | ||

```html
<!DOCTYPE html>
<html lang="en">
<head>
<meta charset="utf-8">
<title>Harlow Hauling Stationery</title>
<link href="https://fonts.googleapis.com/css2?family=Open+Sans:wght@400;600;700&display=swap" rel="stylesheet">
<style>
:root{
  --green:#2f9e3c;
  --green-dark:#1f7a2b;
  --ink:#3b3b3b;
  --grey:#8a8a8a;
  --grey-light:#d6d6d6;
  --charcoal:#3a3c3e;
  --paper:#ffffff;
  --bg:#ffffff;
}
*{box-sizing:border-box;margin:0;padding:0}
html,body{width:1200px;height:559px;overflow:hidden;background:var(--bg)}
body{font-family:"Open Sans",Arial,sans-serif;color:var(--ink);position:relative}
.sheet,.card,.envelope,.envelope-back{position:absolute;background:var(--paper);box-shadow:0 1px 4px rgba(0,0,0,.25);overflow:hidden}

/* brand mark */
.brand{display:flex;flex-direction:column;align-items:center;gap:3px}
.brand-dot{width:26px;height:26px;border-radius:50%;background:var(--green)}
.brand-name{font-weight:700;color:var(--green);font-size:8px;letter-spacing:.5px;white-space:nowrap}

/* letterhead */
.letterhead-back{left:72px;top:42px;width:338px;height:500px}
.letterhead{left:14px;top:12px;width:345px;height:492px;padding:24px 26px}
.letterhead .brand{position:absolute;left:22px;top:26px}
.letterhead .brand-dot{width:40px;height:40px}
.letterhead .brand-name{font-size:9px}
.contact{position:absolute;right:24px;top:18px;font-size:5.5px;line-height:9px;color:var(--grey)}
.contact li{list-style:none;display:flex;align-items:center;gap:4px}
.contact i{display:inline-block;width:5px;height:5px;border-radius:50%;background:var(--green)}
.recipient{position:absolute;left:26px;top:98px;font-size:5.5px;line-height:8px}
.letter-body{position:absolute;left:26px;top:140px;width:290px;font-size:5.6px;line-height:8.2px;color:#555}
.letter-body p{margin-bottom:7px}
.signature{position:absolute;left:26px;top:420px;width:50px;height:18px;background:linear-gradient(90deg,#c9d2e6,#e8ecf5);border-radius:8px}
.seal{position:absolute;left:86px;top:412px;width:28px;height:28px;border-radius:50%;background:#b9bfd6}
.signer{position:absolute;left:26px;top:442px;font-size:5.5px;line-height:8px}
.wave{position:absolute;left:0;bottom:0;width:100%}

/* cards */
.card{width:112px;height:66px;top:28px}
.card-front{left:468px}
.card-front .brand{position:absolute;left:14px;top:12px}
.card-info{left:588px}
.card-info .name{position:absolute;left:58px;top:8px;font-size:6px;font-weight:700;color:var(--green)}
.card-info .role{position:absolute;left:58px;top:16px;font-size:4.5px;color:var(--grey)}
.card-info ul{position:absolute;left:58px;top:28px;font-size:4px;line-height:6.5px;list-style:none;color:var(--ink)}
.card-info .side{position:absolute;left:0;top:0;width:50px;height:100%;background:linear-gradient(160deg,#e4e4e4,#b6b6b6)}
.card-dark{left:710px;background:var(--charcoal)}
.card-dark .brand{position:absolute;right:12px;top:20px}
.card-dark .brand-dot{width:16px;height:16px}
.card-dark .side{position:absolute;left:0;top:0;width:52px;height:100%;background:linear-gradient(135deg,#5c5e60,#2c2d2e)}

/* front envelopes */
.envelope{left:362px;width:358px;height:178px}
.envelope-one{top:168px}
.envelope-two{top:372px}
.envelope .brand{position:absolute;left:30px;top:18px}
.envelope .brand-dot{width:30px;height:30px}
.return{position:absolute;left:22px;top:66px;font-size:4.5px;color:var(--grey)}

/* envelope backs */
.envelope-back{left:734px;width:444px}
.back-one{top:172px;height:120px}
.back-two{top:298px;height:124px;background:linear-gradient(180deg,#8e8e8e,#6a6a6a)}
.back-three{top:424px;height:126px}
.flap{position:absolute;left:0;top:0;width:100%;height:100%}
.flap-dot{position:absolute;left:50%;width:16px;height:16px;margin-left:-8px;border-radius:50%;background:var(--green)}
</style>
</head>
<body>

<!-- Letterhead -->
<div class="sheet letterhead-back">
  <div class="wave" role="img" aria-label="Grey wave pattern band" style="height:60px;background:linear-gradient(180deg,rgba(255,255,255,0),#bdbdbd 40%,#5a5a5a)"></div>
</div>

<div class="sheet letterhead">
  <div class="brand"><span class="brand-dot"></span><span class="brand-name">HARLOW HAULING</span></div>
  <ul class="contact">
    <li><i></i>(603) 555-0142</li>
    <li><i></i>pinecarrier@velmorapost.net</li>
    <li><i></i>5810 County Road 7</li>
    <li><i></i>Canaan, NH 03598</li>
  </ul>
  <div class="recipient">Recipient Name<br>Main Street Office<br>Town, State</div>
  <div class="letter-body">
    <p>Dear Customer,</p>
    <p>Thank you for choosing our team for your upcoming move. We handle every piece of fine furniture with padded blankets, careful wrapping and trained hands, so your home arrives exactly as it left.</p>
    <p>Our crew plans each route in advance, measures doorways and stairs, and protects floors before the first item is lifted. Large antiques, pianos and glass cabinets receive extra attention and secure straps.</p>
    <p>Delivery windows are confirmed the day before, and our driver calls when on the way. You will always know where your belongings are.</p>
    <p>Please reach out with any questions about scheduling, storage or insurance. We look forward to working with you.</p>
    <p>Sincerely,</p>
  </div>
  <div class="signature" role="img" aria-label="Handwritten signature"></div>
  <div class="seal"></div>
  <div class="signer">Danny Crebbe<br>Owner</div>
  <svg class="wave" viewBox="0 0 345 60" height="60" preserveAspectRatio="none">
    <path d="M0 24 C110 58 220 52 345 6 L345 60 L0 60 Z" fill="var(--green)"/>
    <path d="M0 40 C120 62 230 56 345 26 L345 60 L0 60 Z" fill="var(--green-dark)"/>
  </svg>
</div>

<!-- Business cards -->
<div class="card card-front">
  <div class="brand"><span class="brand-dot" style="width:20px;height:20px"></span><span class="brand-name" style="font-size:6px">HARLOW HAULING</span></div>
  <svg style="position:absolute;right:0;top:0" width="40" height="66" viewBox="0 0 40 66">
    <path d="M40 0 L40 66 L8 66 C26 44 20 22 40 0 Z" fill="var(--green)"/>
  </svg>
</div>

<div class="card card-info">
  <div class="side"></div>
  <div class="name">Danny Crebbe</div>
  <div class="role">Owner</div>
  <ul>
    <li>(603) 555-0142</li>
    <li>pinecarrier@velmorapost.net</li>
    <li>5810 County Road 7</li>
    <li>Canaan, NH 03598</li>
  </ul>
</div>

<div class="card card-dark">
  <div class="side"></div>
  <svg style="position:absolute;left:30px;top:0" width="40" height="66" viewBox="0 0 40 66">
    <path d="M0 66 C18 44 14 20 36 0 L40 0 C22 24 26 46 10 66 Z" fill="var(--green)"/>
  </svg>
  <div class="brand"><span class="brand-dot"></span><span class="brand-name" style="font-size:6px">HARLOW HAULING</span></div>
</div>

<!-- Front envelopes -->
<div class="envelope envelope-one">
  <div class="brand"><span class="brand-dot"></span><span class="brand-name">HARLOW HAULING</span></div>
  <div class="return">5810 County Road 7, Canaan, NH 03598</div>
  <svg class="wave" viewBox="0 0 358 60" height="60" preserveAspectRatio="none">
    <path d="M0 10 C80 10 150 40 230 60 L0 60 Z" fill="var(--green)"/>
    <path d="M150 60 C230 36 300 40 358 20 L358 60 Z" fill="var(--grey-light)"/>
  </svg>
</div>

<div class="envelope envelope-two">
  <div class="brand"><span class="brand-dot"></span><span class="brand-name">HARLOW HAULING</span></div>
  <div class="return">5810 County Road 7, Canaan, NH 03598</div>
  <svg class="wave" viewBox="0 0 358 60" height="60" preserveAspectRatio="none">
    <path d="M0 10 C80 10 150 40 230 60 L0 60 Z" fill="var(--green)"/>
    <path d="M150 60 C230 36 300 40 358 20 L358 60 Z" fill="var(--grey-light)"/>
  </svg>
</div>

<!-- Envelope backs -->
<div class="envelope-back back-one">
  <svg class="flap" viewBox="0 0 444 120" preserveAspectRatio="none">
    <rect width="444" height="14" fill="var(--green)"/>
    <path d="M0 14 L222 62 L444 14" fill="none" stroke="#cfcfcf" stroke-width="1"/>
  </svg>
  <span class="flap-dot" style="top:50px"></span>
</div>

<div class="envelope-back back-two">
  <svg class="flap" viewBox="0 0 444 124" preserveAspectRatio="none">
    <path d="M0 0 L222 58 L444 0 Z" fill="#5a5a5a"/>
    <path d="M0 0 L222 58 L444 0" fill="none" stroke="#9a9a9a" stroke-width="1"/>
  </svg>
  <span class="flap-dot" style="top:46px"></span>
</div>

<div class="envelope-back back-three">
  <svg class="flap" viewBox="0 0 444 126" preserveAspectRatio="none">
    <path d="M0 0 L222 60 L444 0" fill="none" stroke="#cfcfcf" stroke-width="1"/>
  </svg>
  <span class="flap-dot" style="top:48px"></span>
</div>

</body>
</html>
```